Trade Show Banner "Brindlequay"

1.7' x 3' vertical banner to complement trade show booth panels (3-panel tabletop booth attached). The word file (attached) is for text and not meant to imply design. We manage homeowner and condo associations that are run by volunteer boards of directors who already have full-time jobs or who may have no training in how to run an organization. It can be highly stressful and not very rewarding. We want this poster/banner to convey that feeling of stress along with a hope for relief and relaxation. Our logo is attached. The full logo is the top one in the file. You may also want to use the triangle (attached) in addition to or instead of the logo. Our corporate fonts are attached. Please let me know if you need additional information or if you feel like there is too much copy or any other thoughts or comments you have.

Target Market(s)

Volunteer boards of directors for homeowner and condo associations--all ages, genders, races, occupations.

Industry/Entity Type

Property Management

Other font styles liked:
• "Copper Lantern" is part of a trademark and should be in Mistral with the green from our logo

Requirements
Must have
• Simple, easy to read, don't clash with booth design
Nice to have
• convey the tension of stress contrasted with the feeling of relaxation and relief.

```html
<!DOCTYPE html>
<html lang="en">
<head>
<meta charset="utf-8">
<title>Brindlequay – Trade Show Banner</title>
<link href="https://fonts.googleapis.com/css2?family=PT+Sans:ital,wght@0,400;0,700;1,400;1,700&display=swap" rel="stylesheet">
<style>
  :root {
    --wall-light: #f1f1f0;
    --wall-mid: #e2e3e2;
    --ink: #141414;
    --accent-red: #b3171c;
    --rule: #3a3a3a;
    --tri-rose: #c9979d;
    --tri-blue: #a3a5da;
    --tri-green: #b3d8a6;
    --brand-maroon: #6e1424;
  }
  html, body {
    margin: 0;
    padding: 0;
    overflow: hidden;
  }
  .banner {
    position: relative;
    width: 680px;
    height: 1200px;
    overflow: hidden;
    background: radial-gradient(ellipse at 50% 40%, var(--wall-light) 0%, var(--wall-mid) 100%);
    font-family: "PT Sans", Arial, sans-serif;
    color: var(--ink);
  }
  .triangles {
    position: absolute;
    inset: 0;
  }
  .eyebrow {
    position: absolute;
    top: 78px;
    left: 0;
    width: 100%;
    text-align: center;
    font-family: Arial, Helvetica, sans-serif;
    font-weight: 400;
    font-size: 42px;
    color: var(--accent-red);
    line-height: 52px;
    margin: 0;
  }
  .title {
    position: absolute;
    top: 135px;
    left: 0;
    width: 100%;
    text-align: center;
    font-weight: 700;
    font-size: 86px;
    line-height: 100px;
    letter-spacing: 0.5px;
    margin: 0;
  }
  .pair {
    position: absolute;
    left: 30px;
    width: 620px;
    text-align: center;
    font-style: italic;
    margin: 0;
  }
  .pair .stress {
    display: block;
    font-weight: 700;
    font-size: 23px;
    line-height: 28px;
  }
  .pair .relief {
    display: block;
    font-weight: 400;
    font-size: 20.5px;
    line-height: 25.5px;
    margin-top: 3px;
  }
  .pair--wide { left: 20px; width: 640px; }
  .pair--1 { top: 302px; }
  .pair--2 { top: 418px; }
  .pair--3 { top: 530px; }
  .pair--4 { top: 646px; }
  .pair--5 { top: 788px; }
  .pair--5 .relief { margin-top: 8px; }

  .brand {
    position: absolute;
    top: 1000px;
    left: 0;
    width: 100%;
    display: flex;
    justify-content: center;
    align-items: center;
    gap: 16px;
  }
  .brand-mark {
    width: 58px;
    height: 58px;
    background: var(--brand-maroon);
  }
  .brand-name {
    font-weight: 700;
    font-size: 30px;
    line-height: 34px;
    color: var(--ink);
    margin: 0;
  }
</style>
</head>
<body>
  <div class="banner">
    <svg class="triangles" width="680" height="1200" viewBox="0 0 680 1200" aria-hidden="true">
      <polygon points="340,328 516,598 164,598" fill="var(--tri-rose)" fill-opacity="0.8"/>
      <polygon points="164,600 328,870 0,870" fill="var(--tri-blue)" fill-opacity="0.85"/>
      <polygon points="516,600 680,870 344,870" fill="var(--tri-green)" fill-opacity="0.85"/>
      <line x1="80" y1="139" x2="600" y2="139" stroke="var(--rule)" stroke-width="1"/>
      <line x1="80" y1="387" x2="630" y2="387" stroke="var(--rule)" stroke-width="1.5" stroke-opacity="0.6"/>
      <line x1="80" y1="501" x2="630" y2="501" stroke="var(--rule)" stroke-width="1.5" stroke-opacity="0.6"/>
      <line x1="80" y1="614" x2="630" y2="614" stroke="var(--rule)" stroke-width="1.5" stroke-opacity="0.6"/>
      <line x1="80" y1="754" x2="630" y2="754" stroke="var(--rule)" stroke-width="1.5" stroke-opacity="0.6"/>
    </svg>

    <p class="eyebrow">THE ART OF</p>
    <h1 class="title">Brindlequay</h1>

    <p class="pair pair--1">
      <span class="stress">Stress: THE BOARD HAS TOO MUCH WORK TO DO</span>
      <span class="relief">Relax…and let us do the work.</span>
    </p>
    <p class="pair pair--2">
      <span class="stress">Stress: YOUR COMMUNITY HAS “ISSUES.”</span>
      <span class="relief">Relax…and let us give you a Copper Lantern.</span>
    </p>
    <p class="pair pair--3">
      <span class="stress">Stress: YOUR MEMBERS CANNOT PAY ONLINE.</span>
      <span class="relief">Relax…we’ll give your members multiple ways to pay.</span>
    </p>
    <p class="pair pair--wide pair--4">
      <span class="stress">Stress: COMMUNICATION IS POOR OR INCONSISTENT.</span>
      <span class="relief">Relax…we’ll keep you informed with a robust online portal,<br>chock full of information.</span>
    </p>
    <p class="pair pair--wide pair--5">
      <span class="stress">Stress: YOUR DELINQUENCIES ARE HIGH.</span>
      <span class="relief">Relax…as a licensed collection agency, we have developed<br>an effective collections program that works in tandem<br>with your collections attorney. Plus, we can report to the<br>credit bureau!</span>
    </p>

    <div class="brand">
      <div class="brand-mark"></div>
      <p class="brand-name">Harrowfield<br>Management, Inc.</p>
    </div>
  </div>
</body>
</html>
```